Yoga for Scoliosis business card/logo design

I need a business card/logo design for my new business. I am a registered yoga teacher and am certified in yoga for scoliosis. I'd like my card to read "Marlow Yoga Yoga for a Healthy Spine" and would like to incorporate one of the letters in my name{ ie the first vertical line of the letter " H "or "D"} to resemble a scoliotic spine. I regularly teach the following:Yoga for Scoliosis, Yoga for Back Health, Hatha yoga, Vinyasa yoga with Iyengar style alignment. This business is mostly for private clients, but I also teach group, semi-private & work shop classes. I like the colors green (light emerald) and royal blue. I'd like the design to be somewhat sleek, but not too modern. I also like the idea of a ying/yang symbol with a scoliotic spine dviding it.

Industry/Entity Type

Teacher

Contact Information for Business Card

Tamsin Marlow
200 RYT, Certified Yoga for Scoliosis Instructor
MarlowYoga.example
MarlowYoga@mailbox.example
415-629-3174

```html
<!DOCTYPE html>
<html lang="en">
<head>
<meta charset="utf-8">
<title>Marlow Yoga for a Healthy Spine — Business Card Options</title>
<link href="https://fonts.googleapis.com/css2?family=Dancing+Script:wght@500&family=Roboto+Condensed:wght@400&display=swap" rel="stylesheet">
<style>
  :root {
    --page: #ffffff;
    --plum-text: #e6d6ee;
    --plum-title: #e9dbf0;
    --sky-text: #55b4e4;
    --white: #ffffff;
  }
  html, body {
    margin: 0;
    padding: 0;
    width: 710px;
    height: 1200px;
    overflow: hidden;
    background: var(--page);
  }
  .sheet { position: relative; width: 710px; height: 1200px; }
  .card {
    position: absolute;
    left: 28px;
    overflow: hidden;
    font-family: "Roboto Condensed", "Arial Narrow", sans-serif;
  }
  .card__bg { position: absolute; inset: 0; width: 100%; height: 100%; }
  .card__title {
    position: absolute;
    left: 0; right: 0;
    margin: 0;
    text-align: center;
    white-space: nowrap;
    font-family: "Dancing Script", cursive;
    font-weight: 500;
    line-height: 1;
  }
  .card__contact { position: absolute; margin: 0; padding: 0; list-style: none; }
  .card__contact li {
    position: absolute;
    left: 0;
    white-space: nowrap;
    display: flex;
    align-items: center;
    gap: 10px;
    line-height: 1;
  }
  .icon { width: 18px; height: 20px; flex: none; text-align: center; }
  .emblem { position: absolute; }

  .card--plum { top: 32px; width: 656px; height: 366px; }
  .card--plum .card__title { top: 36px; font-size: 46px; color: var(--plum-title); }
  .card--plum .card__contact { left: 38px; top: 0; color: var(--plum-text); font-size: 22px; }

  .card--night { top: 414px; width: 658px; height: 367px; }
  .card--night .card__title { top: 34px; font-size: 46px; color: var(--sky-text); }
  .card--night .card__contact { left: 38px; top: 0; color: var(--sky-text); font-size: 22px; }

  .card--mint { top: 797px; width: 658px; height: 368px; }
  .card--mint .card__title { top: 36px; font-size: 51px; color: var(--white); }
  .card--mint .card__contact { left: 32px; top: 0; color: var(--white); font-size: 23px; }
</style>
</head>
<body>
<main class="sheet">

  <section class="card card--plum">
    <svg class="card__bg" viewBox="0 0 656 366" preserveAspectRatio="none" aria-hidden="true">
      <defs>
        <linearGradient id="plumFill" x1="0" y1="0" x2="0" y2="1">
          <stop offset="0" stop-color="#7f5b9b"/>
          <stop offset="1" stop-color="#4b1f5f"/>
        </linearGradient>
        <linearGradient id="plumWave" x1="0" y1="0" x2="1" y2="0">
          <stop offset="0" stop-color="#b79bc4"/>
          <stop offset="1" stop-color="#f3e6ef"/>
        </linearGradient>
        <linearGradient id="plumLow" x1="0" y1="0" x2="0" y2="1">
          <stop offset="0" stop-color="#b89cc6"/>
          <stop offset="1" stop-color="#6a3a7e"/>
        </linearGradient>
      </defs>
      <rect width="656" height="366" fill="url(#plumFill)"/>
      <path d="M0 282 C120 250 250 270 360 300 C470 325 560 270 656 220 L656 366 L0 366 Z" fill="url(#plumWave)" opacity="0.85"/>
      <path d="M0 300 C130 280 250 300 360 320 C470 340 570 300 656 260 L656 366 L0 366 Z" fill="url(#plumLow)" opacity="0.9"/>
    </svg>
    <h1 class="card__title">Marlow Yoga for a Healthy Spine</h1>
    <ul class="card__contact">
      <li style="top:106px"><svg class="icon" viewBox="0 0 18 20"><circle cx="9" cy="6" r="4.5" fill="currentColor"/><path d="M1 19 C2 12 16 12 17 19 Z" fill="currentColor"/></svg>Tamsin Marlow 200 RYT, Certified Yoga for Scoliosis Instructor</li>
      <li style="top:148px"><svg class="icon" viewBox="0 0 18 20"><rect x="4" y="1" width="10" height="18" rx="2" fill="none" stroke="currentColor" stroke-width="1.5"/></svg>415-629-3174</li>
      <li style="top:190px"><span class="icon">@</span>MarlowYoga@mailbox.example</li>
      <li style="top:232px"><svg class="icon" viewBox="0 0 18 20"><circle cx="9" cy="10" r="8" fill="currentColor"/><path d="M1 10 H17 M9 2 V18" stroke="#4b1f5f" stroke-width="0.8"/></svg>MarlowYoga.example</li>
    </ul>
    <svg class="emblem" style="left:464px;top:188px" width="174" height="154" viewBox="0 0 174 154" role="img" aria-label="Meditating figure with a curved spine">
      <ellipse cx="87" cy="77" rx="84" ry="74" fill="none" stroke="#d9c6e2" stroke-width="3"/>
      <ellipse cx="87" cy="82" rx="60" ry="62" fill="#9a7cb0" opacity="0.55"/>
    </svg>
  </section>

  <section class="card card--night">
    <svg class="card__bg" viewBox="0 0 658 367" preserveAspectRatio="none" aria-hidden="true">
      <defs>
        <linearGradient id="nightFill" x1="0" y1="0" x2="0" y2="1">
          <stop offset="0" stop-color="#08141b"/>
          <stop offset="1" stop-color="#0a3442"/>
        </linearGradient>
      </defs>
      <rect width="658" height="367" fill="url(#nightFill)"/>
      <path d="M0 272 C120 250 240 262 350 292 C460 320 570 270 658 215 L658 367 L0 367 Z" fill="#020a0e" opacity="0.9"/>
      <path d="M0 292 C130 276 250 296 360 312 C470 328 570 296 658 262 L658 367 L0 367 Z" fill="#0b3644"/>
    </svg>
    <h1 class="card__title">Marlow Yoga for a Healthy Spine</h1>
    <ul class="card__contact">
      <li style="top:107px"><svg class="icon" viewBox="0 0 18 20"><circle cx="9" cy="6" r="4.5" fill="currentColor"/><path d="M1 19 C2 12 16 12 17 19 Z" fill="currentColor"/></svg>Tamsin Marlow 200 RYT, Certified Yoga for Scoliosis Instructor</li>
      <li style="top:149px"><svg class="icon" viewBox="0 0 18 20"><rect x="4" y="1" width="10" height="18" rx="2" fill="none" stroke="currentColor" stroke-width="1.5"/></svg>415-629-3174</li>
      <li style="top:191px"><span class="icon">@</span>MarlowYoga@mailbox.example</li>
      <li style="top:233px"><svg class="icon" viewBox="0 0 18 20"><circle cx="9" cy="10" r="8" fill="currentColor"/><path d="M1 10 H17 M9 2 V18" stroke="#08141b" stroke-width="0.8"/></svg>MarlowYoga.example</li>
    </ul>
    <svg class="emblem" style="left:466px;top:204px" width="166" height="134" viewBox="0 0 166 134" role="img" aria-label="Meditating figure with a curved spine">
      <ellipse cx="83" cy="67" rx="80" ry="64" fill="none" stroke="#4aa4d6" stroke-width="3"/>
      <ellipse cx="83" cy="72" rx="56" ry="54" fill="#2f7fac" opacity="0.6"/>
    </svg>
  </section>

  <section class="card card--mint">
    <svg class="card__bg" viewBox="0 0 658 368" preserveAspectRatio="none" aria-hidden="true">
      <defs>
        <linearGradient id="mintFill" x1="0" y1="0" x2="0" y2="1">
          <stop offset="0" stop-color="#5bdb95"/>
          <stop offset="1" stop-color="#47d184"/>
        </linearGradient>
      </defs>
      <rect width="658" height="368" fill="url(#mintFill)"/>
      <path d="M0 312 C140 300 260 300 380 290 C500 280 580 240 658 200 L658 368 L0 368 Z" fill="#8fe8b6" opacity="0.55"/>
    </svg>
    <h1 class="card__title">Marlow Yoga for a Healthy Spine</h1>
    <ul class="card__contact">
      <li style="top:150px"><svg class="icon" viewBox="0 0 18 20"><circle cx="9" cy="6" r="4.5" fill="currentColor"/><path d="M1 19 C2 12 16 12 17 19 Z" fill="currentColor"/></svg>Tamsin Marlow 200 RYT, Certified Yoga for Scoliosis Instructor</li>
      <li style="top:194px"><svg class="icon" viewBox="0 0 18 20"><rect x="4" y="1" width="10" height="18" rx="2" fill="none" stroke="currentColor" stroke-width="1.5"/></svg>415-629-3174</li>
      <li style="top:239px"><span class="icon">@</span>MarlowYoga@mailbox.example</li>
      <li style="top:282px"><svg class="icon" viewBox="0 0 18 20"><circle cx="9" cy="10" r="8" fill="currentColor"/><path d="M1 10 H17 M9 2 V18" stroke="#47d184" stroke-width="0.8"/></svg>MarlowYoga.example</li>
    </ul>
    <svg class="emblem" style="left:464px;top:203px" width="176" height="142" viewBox="0 0 176 142" role="img" aria-label="Meditating figure with a curved spine">
      <ellipse cx="88" cy="71" rx="84" ry="67" fill="none" stroke="#ffffff" stroke-width="3.5"/>
      <ellipse cx="88" cy="76" rx="58" ry="58" fill="#ffffff" opacity="0.55"/>
    </svg>
  </section>

</main>
</body>
</html>
```